Family Farm Produce poster design

I have attached a ps file of a rough design i am after for a flow chart on our family farm and how people can buy our produce. I would like someone to tidy it up and make it look great. Using the same font (KG Second Chances Sket...) and similar photos (please message me for more photos if needed) . I am after a PS file of the design as details change from time to time .

Industry/Entity Type

Farm

```html
<!DOCTYPE html>
<html lang="en">
<head>
<meta charset="utf-8">
<title>Brookvale Produce Family Farm</title>
<link href="https://fonts.googleapis.com/css2?family=Cabin+Sketch:wght@700&family=Bree+Serif&display=swap" rel="stylesheet">
<style>
  :root {
    --sky-top: #9bdaf8;
    --sky-low: #e9f7fd;
    --paper: #ffffff;
    --pale-blue: #cdeffb;
    --green: #3ec43a;
    --green-dark: #2fa52c;
    --red: #ee2024;
    --pink: #e87878;
    --blue-bar: #0793cc;
    --red-bar: #e0504a;
    --orange-bar: #f7b24c;
    --brand: #e56a6a;
    --cow: #7a2a10;
    --egg: #e0a24a;
    --photo-hill: #5e9a3c;
    --photo-valley: #637f6a;
    --photo-pasture: #6a9e48;
  }
  * { margin: 0; padding: 0; box-sizing: border-box; }
  html, body { width: 1199px; height: 1200px; overflow: hidden; }
  body { font-family: "Bree Serif", serif; }
  .poster {
    position: relative; width: 1199px; height: 1200px; overflow: hidden;
    background: linear-gradient(180deg, var(--sky-top) 0, var(--sky-low) 420px, var(--paper) 480px, var(--paper) 618px, var(--pale-blue) 618px);
  }
  .abs { position: absolute; }
  .sketch { font-family: "Cabin Sketch", cursive; font-weight: 700; }
  .brand {
    left: 0; width: 1199px; top: 98px;
    display: flex; justify-content: center; align-items: center; gap: 12px;
    font-size: 30px; color: var(--brand); letter-spacing: 1px;
  }
  .brand .dot { width: 22px; height: 22px; border-radius: 50%; background: var(--brand); }
  .title {
    left: 0; width: 1199px; top: 222px; text-align: center;
    font-size: 60px; color: var(--green); letter-spacing: 1px;
  }
  .bubble-text { text-align: center; color: #fff; letter-spacing: 2px; }
  .how { left: 324px; top: 318px; width: 550px; height: 68px; line-height: 68px; font-size: 56px; }
  .what { left: 389px; top: 658px; width: 422px; height: 58px; line-height: 58px; font-size: 41px; }
  .col { width: 380px; text-align: center; }
  .col h2 { font-family: "Cabin Sketch", cursive; font-weight: 700; font-size: 47px; color: var(--green); line-height: 1; }
  .col p { font-size: 31px; color: var(--green-dark); margin-top: 8px; }
  .product h3 { font-family: "Cabin Sketch", cursive; font-weight: 700; font-size: 38px; color: var(--pink); line-height: 1; }
  .product p { font-size: 31px; color: var(--pink); margin-top: 4px; }
  .why { left: 380px; width: 440px; top: 768px; text-align: center; color: var(--red); }
  .why h3 { font-size: 31px; font-weight: 400; display: inline-block; border-bottom: 3px solid var(--red); padding-bottom: 2px; width: 310px; }
  .why ul { list-style: none; margin-top: 10px; font-size: 26px; line-height: 40px; }
  .why li::before { content: ""; display: inline-block; width: 12px; height: 12px; border-radius: 50%; background: var(--red); border: 2px solid #f7a0a0; margin-right: 8px; vertical-align: 3px; }
</style>
</head>
<body>
<main class="poster">
  <div class="abs brand"><span class="dot"></span><span>BROOKVALE PRODUCE</span></div>

  <h1 class="abs title sketch">Brookvale Produce Family Farm</h1>

  <svg class="abs" style="left:0;top:0" width="1199" height="620" aria-hidden="true">
    <path d="M324 318 H864 Q874 318 874 328 V376 Q874 386 864 386 H612 L600 432 L588 386 H324 Z" fill="var(--green)"/>
    <path d="M51 450 H417 V466 H246 L234 486 L222 466 H51 Z" fill="var(--blue-bar)"/>
    <path d="M418 450 H784 V466 H613 L601 486 L589 466 H418 Z" fill="var(--red-bar)"/>
    <path d="M787 450 H1152 V466 H982 L970 486 L958 466 H787 Z" fill="var(--orange-bar)"/>
  </svg>
  <div class="abs bubble-text sketch how">HOW DO WE FARM?</div>

  <div class="abs col" style="left:54px;top:512px"><h2>Organic</h2><p>(Chemical Free)</p></div>
  <div class="abs col" style="left:410px;top:512px"><h2>Nutrient Dense</h2><p>(Add Life To Soil)</p></div>
  <div class="abs col" style="left:764px;top:512px"><h2>Pasture Raised</h2><p>(Outdoors + Moving)</p></div>

  <svg class="abs" style="left:0;top:640px" width="1199" height="140" aria-hidden="true">
    <path d="M399 18 H811 V66 Q811 76 801 76 H612 L600 120 L588 76 H389 V28 Q389 18 399 18 Z" fill="var(--red)"/>
  </svg>
  <div class="abs bubble-text sketch what">WHAT DO WE FARM?</div>

  <div class="abs" role="img" aria-label="Illustration of a brown cow with a premium quality ribbon" style="left:154px;top:734px;width:192px;height:116px;background:var(--cow);border-radius:40px 30px 20px 20px"></div>
  <div class="abs col product" style="left:51px;top:862px"><h3>BEEF</h3><p>(100% grass Fed)</p></div>

  <div class="abs why">
    <h3>WHY BUY FROM US?</h3>
    <ul>
      <li>Meat ready portions</li>
      <li>Buy only the cuts you want</li>
      <li>buy bulk and save</li>
    </ul>
  </div>

  <div class="abs" role="img" aria-label="Illustration of a wicker basket full of brown eggs" style="left:894px;top:732px;width:106px;height:96px;background:var(--egg);border-radius:50% 50% 45% 45%"></div>
  <div class="abs col product" style="left:766px;top:866px"><h3>EGGS</h3><p>(Fresh Delicious)</p></div>

  <svg class="abs" style="left:0;top:955px" width="1199" height="245" role="img" aria-label="Farm landscape photos: cattle grazing a green hill, misty mountain valley, and chickens on open pasture">
    <path d="M256 60 Q510 -30 750 85 L750 245 L256 245 Z" fill="var(--photo-valley)"/>
    <path d="M600 245 Q800 20 1199 18 L1199 245 Z" fill="var(--photo-pasture)"/>
    <path d="M0 33 Q260 -10 430 40 Q500 120 520 245 L0 245 Z" fill="var(--photo-hill)"/>
  </svg>
</main>
</body>
</html>
```